Stick and Box Packaging for Coffee

We are looking to have tube and stick designs (packaging) for our coffee product.
Use these two different kinds of packaging for your design references.

1. http://www.plivorant.com/market-we-serve/beverages/coffee
2. http://www.grabomix.com/reclosable-tubes.html

Please include a RED color somewhere on the design. May be a border line or just come up with the design. Please see the attached images as reference.

Estimated Dimension:
1. Height - 0.88 inches
2. Length - 4.50 inches

sample color palettes:
Brown
Black
Red
Green
Golden Brown

*Please make the packaging look like a premium/high end packaging.

For the meantime - please use "Tundra Coffee" as the brand name also make a sample logo for it. For the Nutrifacts and other write up, just use a sample information.

By the way, this product is VERDAmark and FRAB Organic Certified. Please do not add the nutrifacts on the sticks just write it on the box. Make the box the same design as Quelvane cigarette and the color texture a mix of glossy and matte texture.

Please use the images from this link as your additional reference for the stick and box sizes and other information

http://shpq.to/7KuwPmd

Happy New Year and Happy Designing!!!

Target Market(s)

High End and Upscale consumers

Industry/Entity Type

Product

Requirements
Must have
• Sample logo - you can use any logo just for the design then once we have the final logo I will send it to the winner.
• Additional info: Please showcase the Stick design on the box as well like the one from the Coconut Sugar packaging but make some originality with the design on are you going to showcase that on the box
Nice to have
• Please create a sample logo for "Tundra Coffee". This is not the final brand that is why we don't want to create a permanent logo. Just a placeholder Logo will do for now - any - so long as it is relevant - and especially not using known brands.

```html
<!DOCTYPE html>
<html lang="en">
<head>
<meta charset="utf-8">
<title>Tundra Coffee – Box Dieline</title>
<link href="https://fonts.googleapis.com/css2?family=Cinzel:wght@400&family=Open+Sans:wght@300;400;600;700&family=Tinos:wght@700&display=swap" rel="stylesheet">
<style>
:root{
  --black:#0c0b0b;
  --band:#141211;
  --gold:#e2a868;
  --gold-soft:#f4c48e;
  --brown-dark:#3e2514;
  --brown:#7a5332;
  --brown-light:#a88059;
  --photo-top:#9a7853;
  --photo-mid:#7a5535;
  --photo-bottom:#4a2a17;
  --red:#8a1f14;
  --red-dark:#5a120b;
  --paper:#f1f0ea;
  --ink:#222;
  --white:#fff;
  --accent-blue:#4ea7e6;
  --accent-yellow:#e7c35a;
}
*{box-sizing:border-box;margin:0;padding:0}
html,body{width:1200px;height:1080px;overflow:hidden;background:var(--white)}
body{position:relative;font-family:"Open Sans",Arial,sans-serif}
.abs{position:absolute}

/* panels */
.panel-black{background:var(--band)}
.flap-top{left:120px;top:0;width:477px;height:138px}
.flap-band{left:120px;top:68px;width:477px;height:10px;background:linear-gradient(var(--gold-soft),var(--brown))}
.bottom-panel{left:120px;top:803px;width:477px;height:137px}

.tab-area{height:160px;top:138px;background:var(--black)}
.tab-frame{top:138px;height:160px;border:3px solid var(--gold);border-top:none;background:linear-gradient(90deg,var(--brown-dark),var(--brown) 45%,var(--brown-light))}
.tab-left{border-left:none;border-bottom-right-radius:10px}
.tab-right{border-right:none;border-bottom-left-radius:10px}

.photo{top:298px;height:382px;background:linear-gradient(var(--photo-top) 0%,var(--photo-mid) 50%,var(--photo-bottom) 100%)}
.rule{height:10px;top:680px;background:linear-gradient(var(--gold-soft),var(--brown))}
.base{top:690px;height:113px}

.tagline{font-family:"Cinzel",serif;color:var(--white);font-size:24px;letter-spacing:.5px;text-align:center;width:477px;top:630px}
.count{color:var(--white);text-align:right;width:120px;font-weight:300}
.count .num{font-size:40px;line-height:40px;letter-spacing:4px;display:block}
.count .unit{font-size:19px;line-height:20px;display:block}

.seal{width:50px;height:50px;border-radius:50%;border:2px solid #9a9a9a;background:#2a2827}
.seal-oval{width:58px;height:40px;border-radius:50%;border:2px solid #8a8a8a;background:transparent}

.brand-plate{background:linear-gradient(var(--red),var(--red-dark));border:3px solid var(--gold);border-radius:14px;display:flex;align-items:center;justify-content:center;text-align:center}
.brand-name{font-family:"Cinzel",serif;color:var(--white);line-height:1.15}

/* left side copy */
.side-left{left:0;top:138px;width:120px;height:665px;background:var(--band)}
.side-copy{left:7px;top:337px;width:108px;font-size:5.4px;line-height:8.4px;color:#ddd;text-align:justify}
.side-copy h3{font-size:8px;color:var(--accent-yellow);font-weight:400;line-height:9px}
.side-copy p{margin-bottom:8px}
.side-copy .hl{color:var(--accent-blue)}

/* right side */
.side-right{left:597px;top:138px;width:125px;height:665px;background:var(--paper)}
.nutri{left:600px;top:342px;width:118px;border:2px solid var(--ink);background:var(--white);padding:2px 3px;font-size:4.4px;line-height:7.6px;color:#555}
.nutri h4{font-style:italic;font-weight:700;color:var(--ink);font-size:10.5px;line-height:11px}
.nutri .row{border-top:.6px solid #999;display:flex;justify-content:space-between}
.nutri .thick{border-top:3px solid var(--ink)}
.side-info{left:598px;width:122px;font-size:5.4px;line-height:7.6px;color:#555}
.side-info b{color:var(--ink)}

.label{font-family:"Tinos",serif;font-weight:700;color:var(--black);font-size:43px;line-height:38px;text-align:center}
</style>
</head>
<body>

<!-- top flap -->
<div class="abs panel-black flap-top"></div>
<div class="abs flap-band"></div>
<div class="abs brand-plate" style="left:313px;top:33px;width:81px;height:80px;border-width:2px;border-radius:9px">
  <span class="brand-name" style="font-size:11px">Tundra<br>Coffee</span>
</div>

<!-- left side -->
<div class="abs side-left"></div>
<svg class="abs" style="left:0;top:138px" width="120" height="162" viewBox="0 0 120 162">
  <polygon points="0,0 120,0 120,160" fill="#6a4428"/>
  <line x1="0" y1="0" x2="120" y2="160" stroke="#e2a868" stroke-width="3"/>
</svg>
<div class="abs side-copy">
  <h3>No Residue and Unbleached</h3>
  <p>*Coconut Sugar is 35 on the glycemic index and is a healthier alternative to white sugar.</p>
  <p>Kaliva Coco Sugar by Palmora Foods is a <span class="hl">healthier alternative</span> to refined sugar. In comparison, regular cane sugar is 100 on the glycemic index while coconut sugar is 35. This allows your body to absorb the coconut sugar slower and reduce spikes in your blood sugar levels. This provides your body more time to use the sugar as energy rather than converting to fat.</p>
  <p>Kaliva Coco Sugar is <span class="hl">high quality, quick to dissolve in your coffee,</span> and does not leave any residue in comparison to other coconut sugar products. Along with our pledge for quality, we employ sustainable and ethical farming practices to produce our product. Our <span class="hl">FRAB Organic certification</span> means that <span class="hl">no chemical food additives</span> were used in the production of Kaliva Coco Sugar.</p>
  <p><span class="hl">Healthy and all natural,</span> coco sugar is sweet with caramel undertones but will not leave hints of coconut in your palate. Use Kaliva Coco Sugar in your coffee or any recipe that would otherwise call for regular sugar.</p>
  <p class="hl">Enjoy!</p>
</div>

<!-- front -->
<div class="abs tab-area" style="left:120px;width:477px"></div>
<div class="abs tab-frame tab-left" style="left:120px;width:211px"></div>
<div class="abs tab-frame tab-right" style="left:377px;width:220px"></div>
<div class="abs photo" style="left:120px;width:477px" role="img" aria-label="Photo of roasted coffee beans behind a white cup of black coffee"></div>
<div class="abs brand-plate" style="left:289px;top:302px;width:129px;height:128px">
  <span class="brand-name" style="font-size:17px">Tundra<br>Coffee</span>
</div>
<div class="abs tagline" style="left:124px">HIGH QUALITY COFFEE</div>
<div class="abs rule" style="left:120px;width:477px"></div>
<div class="abs panel-black base" style="left:120px;width:477px"></div>
<div class="abs seal-oval" style="left:137px;top:752px"></div>
<div class="abs seal" style="left:207px;top:743px"></div>
<div class="abs count" style="left:455px;top:724px"><span class="num">25</span><span class="unit">STICKS</span></div>
<div class="abs panel-black bottom-panel"></div>

<!-- right side -->
<div class="abs side-right"></div>
<svg class="abs" style="left:597px;top:138px" width="125" height="162" viewBox="0 0 125 162">
  <polygon points="0,0 125,0 0,160" fill="#6a4428"/>
  <line x1="125" y1="0" x2="0" y2="160" stroke="#e2a868" stroke-width="3"/>
</svg>
<div class="abs nutri">
  <h4>Nutrition Facts<br>Valeur Nutritive</h4>
  <div>Serving Size 1 tsp / Quantité 1 portion (3.5g)</div>
  <div>Servings Per Pack / Quantité par paquet 25</div>
  <div class="row thick"><span>Amount per serving / Quantité par portion</span></div>
  <div class="row"><span>Calories/Calories 12.6</span></div>
  <div class="row"><span>Calories from Fat / Calories de lipides 0</span></div>
  <div class="row thick"><span>Amount<br>Teneur</span><span>% Daily Value*<br>% Valeur Quotidienne*</span></div>
  <div class="row"><span>Total Fat/Lipides 0g</span><span>0%</span></div>
  <div class="row"><span>Cholesterol/Cholestérol 0mg</span></div>
  <div class="row"><span>Sodium/Sodium 0mg</span></div>
  <div class="row"><span>Total Carbohydrate/Glucides 2.8g</span><span>0%</span></div>
  <div class="row"><span>&nbsp;&nbsp;Dietary Fiber/Fibres 0g</span><span>0%</span></div>
  <div class="row"><span>&nbsp;&nbsp;Sugars/Sucres 2.8g</span><span>0%</span></div>
  <div class="row"><span>Protein/Protéines 0g</span><span>0%</span></div>
  <div class="row thick"><span>Vitamin A/Vitamine A 0% • Vitamin C/Vitamine C 0%</span></div>
  <div class="row"><span>Calcium/Calcium 0% • Iron/Fer 0%</span></div>
  <div class="row thick" style="font-size:3.6px;line-height:5px">*Percent Daily Values are based on a 2,000 calorie diet. Your daily values may be higher or lower depending on your calorie needs and personal energy requirements.</div>
</div>
<div class="abs side-info" style="top:572px">
  <div>Ingredients: Pure and Organic Coconut Sugar</div>
  <div>Ingrédients: Pur sucre organique de noix de coco</div>
</div>
<div class="abs side-info" style="top:600px">
  <div><b>Manufactured for and Distributed by:</b></div>
  <div>Palmora Foods</div>
  <div>Lindel Drive, Harrow Valley</div>
  <div>California, USA</div>
  <div>Certified Organic by</div>
  <div>VERDAmark SA, PH-VM-208</div>
</div>
<div class="abs rule" style="left:597px;width:125px"></div>
<div class="abs panel-black base" style="left:597px;width:125px"></div>

<!-- back -->
<div class="abs tab-area" style="left:722px;width:478px"></div>
<div class="abs tab-frame tab-left" style="left:722px;width:214px"></div>
<div class="abs tab-frame tab-right" style="left:982px;width:218px"></div>
<div class="abs photo" style="left:722px;width:478px" role="img" aria-label="Photo of roasted coffee beans behind a white cup of black coffee"></div>
<div class="abs brand-plate" style="left:893px;top:302px;width:129px;height:128px">
  <span class="brand-name" style="font-size:17px">Tundra<br>Coffee</span>
</div>
<div class="abs tagline" style="left:729px">HIGH QUALITY COFFEE</div>
<div class="abs rule" style="left:722px;width:478px"></div>
<div class="abs panel-black base" style="left:722px;width:478px"></div>
<div class="abs seal-oval" style="left:742px;top:752px"></div>
<div class="abs seal" style="left:811px;top:743px"></div>
<div class="abs count" style="left:1058px;top:724px"><span class="num">25</span><span class="unit">STICKS</span></div>

<!-- panel labels -->
<div class="abs label" style="left:0;top:978px;width:115px">LEFT<br>SIDE</div>
<div class="abs label" style="left:240px;top:952px;width:236px">TOP<br>FRONT<br>BOTTOM</div>
<div class="abs label" style="left:597px;top:978px;width:150px">RIGHT<br>SIDE</div>
<div class="abs label" style="left:900px;top:978px;width:190px">BACK<br>SIDE</div>

</body>
</html>
```